Business Card for Multi-Brand Sportswear Company

We are looking for a business card which represents our company and the multiple brands within it.

The company: Kelvo Athletics (LTD)
The brands: Kelv, TaliMati, VerdantFlex, Grit and Grime

Employees using these cards would be representing Kelvo Athletics, rather than any of the individual brands. You will see a current design within the uploaded files, to give some inspiration. The actual text of the brands is not necessary, but the logos should be on there is some format.

Our creative minds on this are stretched, so we are looking for someone to make this their own, and show us what a good business card should look like.

We may like to get these printed with spot gloss, so keep that in mind with your designs.

www.kelvoathletics.co.uk

Industry/Entity Type

Business

Contact Information for Business Card

Tom Pennington-Hale
Operations Manager
(+44) 1632 960 417
Tom@kelvoathletics.co.uk
www.kelvoathletics.co.uk

Font styles to use
Sans Serif
Other font styles liked:
• Eurostile

Colors
ffffff

Requirements
Nice to have
• Dark (black) background

```html
<!DOCTYPE html>
<html lang="en">
<head>
<meta charset="utf-8">
<title>Kelvo Athletics – Business Card</title>
<link href="https://fonts.googleapis.com/css2?family=Exo+2:wght@400;600;700&display=swap" rel="stylesheet">
<style>
  :root {
    --backdrop: #3a302b;
    --card: #141414;
    --card-edge: #0b0b0b;
    --gloss: #262626;
    --red: #d92a22;
    --white: #ffffff;
    --soft: #d8d8d8;
    --muted: #8a8a8a;
    --badge: #5a4f66;
  }
  * { box-sizing: border-box; margin: 0; padding: 0; }
  html, body { width: 1200px; height: 716px; overflow: hidden; }
  body {
    background: var(--backdrop);
    font-family: "Exo 2", sans-serif;
    position: relative;
  }
  .card {
    position: absolute;
    top: 215px;
    width: 500px;
    height: 286px;
    background: var(--card);
    border: 1px solid var(--card-edge);
    box-shadow: 0 6px 18px rgba(0,0,0,.45);
    overflow: hidden;
  }
  .card--front { left: 70px; }
  .card--back { left: 630px; }

  /* Front: spot-gloss wordmark */
  .front-mark {
    position: absolute;
    left: 0; right: 0; top: 50%;
    transform: translateY(-50%);
    display: flex;
    justify-content: center;
    align-items: center;
    gap: 12px;
    color: var(--gloss);
    font-weight: 700;
    font-size: 34px;
    letter-spacing: 1px;
  }
  .front-mark__dot {
    width: 16px; height: 16px;
    background: var(--gloss);
  }

  /* Back */
  .holder {
    position: absolute;
    left: 0; top: 26px;
    padding-left: 20px;
    border-left: 8px solid var(--red);
  }
  .holder__name {
    color: var(--red);
    font-weight: 700;
    font-size: 19px;
    line-height: 1.1;
  }
  .holder__role {
    color: var(--white);
    font-size: 11px;
    margin-top: 4px;
  }
  .brand-band {
    position: absolute;
    right: 0; top: 92px;
    width: 250px; height: 58px;
    background: var(--red);
    clip-path: polygon(0 0, 100% 0, 100% 100%, 12% 100%);
    display: flex;
    align-items: center;
    justify-content: flex-end;
    padding-right: 16px;
    color: var(--white);
    font-weight: 700;
    font-size: 20px;
  }
  .contact {
    position: absolute;
    left: 20px; top: 150px;
    list-style: none;
    color: var(--white);
    font-size: 12.5px;
  }
  .contact li {
    display: flex;
    align-items: center;
    gap: 8px;
    height: 19px;
  }
  .contact svg { width: 11px; height: 11px; fill: var(--red); flex: none; }
  .contact .accent { color: var(--red); }
  .contact .address { padding-left: 0; margin-top: 4px; color: var(--soft); }
  .brand-row {
    position: absolute;
    right: 18px; bottom: 16px;
    display: flex;
    align-items: center;
    gap: 10px;
  }
  .brand-row span { display: block; }
  .badge-square { width: 24px; height: 18px; background: var(--badge); }
  .badge-box { width: 22px; height: 22px; border: 2px solid var(--red); border-radius: 4px; }
  .badge-bar { width: 40px; height: 10px; background: var(--white); }
  .badge-ring { width: 20px; height: 20px; border: 2px solid var(--muted); border-radius: 50%; }
</style>
</head>
<body>

<section class="card card--front" aria-label="Card front">
  <div class="front-mark">
    <span class="front-mark__dot"></span>
    <span>Kelvo Athletics</span>
  </div>
</section>

<section class="card card--back" aria-label="Card back">
  <div class="holder">
    <p class="holder__name">Dan Whitcombe</p>
    <p class="holder__role">Managing Director</p>
  </div>

  <div class="brand-band">Kelvo Athletics</div>

  <ul class="contact">
    <li>
      <svg viewBox="0 0 12 12"><path d="M2 1h2.5l1 3-1.5 1a7 7 0 0 0 3 3l1-1.5 3 1V11a1 1 0 0 1-1 1C5 12 0 7 0 2a1 1 0 0 1 1-1z"/></svg>
      +44 (0)1632 960583
    </li>
    <li>
      <svg viewBox="0 0 12 12"><circle cx="6" cy="6" r="6"/><circle cx="6" cy="6" r="2.2" fill="#141414"/></svg>
      dan@kelvoathletics.co.uk
    </li>
    <li>
      <svg viewBox="0 0 12 12"><path d="M0 2h12v8H0z"/><path d="M0 2l6 4.5L12 2" fill="none" stroke="#141414" stroke-width="1.2"/></svg>
      www.<span class="accent">kelvoathletics</span>.co.uk
    </li>
    <li class="address">Lower Fold, Ashby, Thornleigh, TN9 4QX</li>
  </ul>

  <div class="brand-row" aria-label="Group brands">
    <span class="badge-square"></span>
    <span class="badge-box"></span>
    <span class="badge-bar"></span>
    <span class="badge-ring"></span>
  </div>
</section>

</body>
</html>
```